QCRB Property Flyer - For Support Coordinators

Revamping our current brochures and social media posts for our properties. We need a clearer, simpler design that would be designed for Support Coordinators. Attached is our current brochure for reference.

Key details to highlight would include:
- Type of property: Studio Apartments with Psychosocial Disability Support located in Inner West
- Accommodation features
- Services

Our logo is also attached, please make the brochure with similar branding colours and fonts.
Updates

Designs look the same

Sick

Font styles to use
Sans Serif
Other font styles liked:
• Montserrat Light and Montserrat Semi Bold

Colors
0054AA
0677BA
7BADD7
CADEEF
E8F1F8

Requirements
Nice to have
• Please refer to this style guide: https://slides.brelvanto.com/deck/7TkpWmzaQ2eRvB41nLx0YsdHc9JuFgE3KoiVta8Xq5Nw/view?mode=shared

```html
<!DOCTYPE html>
<html lang="en">
<head>
<meta charset="utf-8">
<title>Harbour Kin Care – Studio Apartments Brochure</title>
<link rel="stylesheet" href="https://fonts.googleapis.com/css2?family=Montserrat:wght@300;400;500;600&display=swap">
<style>
  :root{
    --bg:#e7e7e6;
    --charcoal:#3a3e4b;
    --charcoal-deep:#2f323d;
    --cyan:#2aa8d9;
    --cyan-soft:#7badd7;
    --ink:#3b3f48;
    --muted:#7a7f88;
    --paper:#ffffff;
    --navy:#1f3a66;
  }
  *{box-sizing:border-box;margin:0;padding:0}
  html,body{width:1200px;height:2707px;overflow:hidden}
  body{background:var(--bg);font-family:"Montserrat",sans-serif;color:var(--ink);position:relative}

  .page{position:absolute;width:540px;height:764px;background:var(--paper);overflow:hidden;box-shadow:0 6px 18px rgba(0,0,0,.12)}
  .photo{position:absolute}

  /* ---------- cover ---------- */
  .cover-large{left:300px;top:50px;transform:scale(1.1111);transform-origin:0 0}
  .cover-header{position:absolute;left:0;top:0;width:100%;height:150px;background:var(--charcoal);display:flex;align-items:center;justify-content:center}
  .brand{display:flex;flex-direction:column;align-items:center;gap:8px}
  .brand-dot{width:26px;height:26px;border-radius:50%;background:var(--cyan)}
  .brand-name{color:#fff;font-weight:400;font-size:9px;letter-spacing:1.5px;text-transform:uppercase}
  .welcome-band{position:absolute;left:0;top:150px;width:100%;height:50px;background:var(--cyan);color:#fff;font-weight:500;font-size:20px;letter-spacing:.5px;display:flex;align-items:center;justify-content:center;text-transform:uppercase}
  .cover-photo{left:0;top:200px;width:100%;height:360px;background:linear-gradient(180deg,#8fc3ea 0%,#cfe3f1 38%,#4a4b50 40%,#2f3035 72%,#8a7f70 100%)}
  .cover-rule{position:absolute;left:0;top:560px;width:100%;height:5px;background:var(--charcoal)}
  .cover-title{position:absolute;left:0;top:596px;width:100%;text-align:center;font-weight:500;font-size:20px;line-height:1.35;text-transform:uppercase;color:var(--ink)}
  .cover-address{position:absolute;left:0;top:666px;width:100%;text-align:center;color:var(--cyan);font-size:12px}
  .cover-edge{position:absolute;left:0;bottom:0;width:100%;height:5px;background:var(--navy)}

  /* ---------- spreads ---------- */
  .spread{position:absolute;left:60px;width:1080px;height:764px}
  .spread .page:first-child{left:0}
  .spread .page:last-child{left:540px}
  .spread-one{top:1000px}
  .spread-two{top:1880px}
  .spread .page:first-child::after{content:"";position:absolute;right:0;top:0;width:24px;height:100%;background:linear-gradient(90deg,rgba(0,0,0,0),rgba(0,0,0,.08))}

  /* back page */
  .back-header{position:absolute;left:0;top:0;width:100%;height:40px;background:var(--charcoal);color:#fff;font-size:11px;font-weight:500;letter-spacing:.5px;display:flex;align-items:center;justify-content:center;text-transform:uppercase}
  .back-map{left:0;top:40px;width:100%;height:290px;background:linear-gradient(135deg,#eeeeee,#d9d9d9)}
  .back-caption{position:absolute;left:34px;top:340px;right:20px;font-size:10.5px;font-weight:500;color:var(--ink)}
  .back-accent{position:absolute;left:0;top:330px;width:18px;height:380px;background:linear-gradient(180deg,var(--cyan),#1f7fa8)}
  .studio-grid{position:absolute;left:34px;top:364px;right:20px;height:332px;display:grid;grid-template-columns:1fr 1fr;grid-template-rows:1fr 1fr;gap:12px}
  .studio{position:relative;background:linear-gradient(160deg,#f2f2f2,#9ea2a7)}
  .studio:nth-child(2){background:linear-gradient(160deg,#d8d9da,#4b4e53)}
  .studio:nth-child(3){background:linear-gradient(160deg,#e9e9e9,#8c9095)}
  .studio:nth-child(4){background:linear-gradient(160deg,#a7c6dd,#6b5d52)}
  .studio-label{position:absolute;left:8px;bottom:8px;font-size:9px;color:#fff;background:rgba(58,62,75,.7);padding:2px 6px}
  .back-footer{position:absolute;left:20px;right:20px;top:716px;height:36px;display:flex;justify-content:space-between;align-items:center}
  .contact{display:flex;align-items:center;gap:6px;font-size:8px;color:var(--ink)}
  .contact-dot{width:16px;height:16px;border-radius:50%;border:1.5px solid var(--charcoal)}

  /* inside left */
  .inside-top{left:0;top:0;width:100%;height:330px;background:linear-gradient(160deg,#f4f4f4 0%,#c9ccd0 55%,#3d4046 100%)}
  .intro-box{position:absolute;left:34px;top:340px;width:230px;height:230px;background:#fff;padding:16px 16px 0 22px;box-shadow:0 2px 8px rgba(0,0,0,.08)}
  .intro-box::before{content:"";position:absolute;left:0;top:0;width:8px;height:100%;background:var(--cyan)}
  .section-title{font-size:11px;font-weight:600;text-transform:uppercase;margin-bottom:8px;letter-spacing:.3px}
  .body-copy{font-size:8.5px;line-height:1.55;font-weight:300;margin-bottom:8px}
  .feature-box{position:absolute;left:264px;top:250px;width:276px;height:300px;background:var(--charcoal);padding:20px 18px;color:#fff}
  .feature-box .section-title{color:var(--cyan);font-weight:500}
  .feature-list{list-style:none;margin-bottom:18px}
  .feature-list li{display:flex;align-items:flex-start;gap:7px;font-size:8.5px;line-height:1.4;margin-bottom:7px;font-weight:300}
  .tick{flex:none;width:10px;height:10px;margin-top:1px}
  .inside-bottom{position:absolute;left:34px;right:20px;top:592px;height:150px;display:flex;gap:14px}
  .inside-bottom .photo{position:relative;flex:1;background:linear-gradient(160deg,#f0f0f0,#7d8085)}
  .inside-bottom .photo:last-child{background:linear-gradient(160deg,#e8e8e8,#4a4c52)}

  /* inside right */
  .bedroom-photo{left:0;top:0;width:100%;height:280px;background:linear-gradient(160deg,#e9eaec 0%,#b7bbc0 50%,#55585e 100%)}
  .facility-band{position:absolute;left:0;top:250px;width:100%;height:220px;background:var(--charcoal);padding:24px 20px;color:#fff}
  .facility-band .section-title{color:var(--cyan);font-weight:500}
  .facility-band .feature-list{width:250px}
  .thumbs{position:absolute;right:20px;top:26px;width:220px;display:grid;grid-template-columns:repeat(3,60px);gap:14px 20px}
  .thumb{width:60px;height:60px;border-radius:50%;background:linear-gradient(160deg,#e5e5e5,#6f7278)}
  .thumb:nth-child(2n){background:linear-gradient(160deg,#cfe1d2,#4d5a4f)}
  .transport-box{position:absolute;left:20px;top:492px;width:310px;height:180px;background:#fff;padding:16px 16px 0 26px;box-shadow:0 2px 8px rgba(0,0,0,.08)}
  .transport-box::before{content:"";position:absolute;left:0;top:0;width:8px;height:100%;background:var(--cyan)}
  .transport-list{list-style:none}
  .transport-list li{display:flex;align-items:center;gap:7px;font-size:8px;margin-bottom:5px;font-weight:300}
  .kitchen-photo{left:350px;top:470px;width:190px;height:294px;background:linear-gradient(160deg,#fafafa,#9a9da2)}
</style>
</head>
<body>

<svg width="0" height="0" style="position:absolute">
  <symbol id="tick" viewBox="0 0 10 10"><circle cx="5" cy="5" r="4.5" fill="none" stroke="#2aa8d9"/><path d="M2.8 5.2l1.5 1.5 3-3.2" fill="none" stroke="#2aa8d9" stroke-width="1.2"/></symbol>
</svg>

<!-- Cover, large -->
<section class="page cover-large">
  <header class="cover-header">
    <div class="brand"><span class="brand-dot"></span><span class="brand-name">Harbour Kin Care</span></div>
  </header>
  <div class="welcome-band">Welcome to Carrowdale</div>
  <div class="photo cover-photo" role="img" aria-label="Photograph of the dark brick apartment building with planted balconies"></div>
  <div class="cover-rule"></div>
  <h1 class="cover-title">Studio apartments for people with<br>a psychosocial disability</h1>
  <p class="cover-address">27 Wren Lane, Carrowdale NSW 2188</p>
  <div class="cover-edge"></div>
</section>

<!-- Back and front cover spread -->
<div class="spread spread-one">
  <section class="page back-page">
    <header class="back-header">Public transport, shops &amp; facilities</header>
    <div class="photo back-map" role="img" aria-label="Street map of the local area marking the building, station and shopping centres"></div>
    <div class="back-accent"></div>
    <p class="back-caption">Studio Apartments with Psychosocial Disability Support located in Inner West</p>
    <div class="studio-grid">
      <div class="studio" role="img" aria-label="Photograph of studio A interior"><span class="studio-label">Single Studio A</span></div>
      <div class="studio" role="img" aria-label="Photograph of studio B kitchen"><span class="studio-label">Single Studio B</span></div>
      <div class="studio" role="img" aria-label="Photograph of studio C bedroom"><span class="studio-label">Single Studio C</span></div>
      <div class="studio" role="img" aria-label="Photograph of studio D balcony view"><span class="studio-label">Single Studio D</span></div>
    </div>
    <footer class="back-footer">
      <span class="contact"><span class="contact-dot"></span>harbourkin.org.au</span>
      <span class="contact"><span class="contact-dot"></span>hello@harbourkin.org.au</span>
      <span class="contact"><span class="contact-dot"></span>1300 482 913</span>
      <span class="contact"><span class="contact-dot"></span>27 Wren Lane, Carrowdale</span>
    </footer>
  </section>

  <section class="page cover-page">
    <header class="cover-header">
      <div class="brand"><span class="brand-dot"></span><span class="brand-name">Harbour Kin Care</span></div>
    </header>
    <div class="welcome-band">Welcome to Carrowdale</div>
    <div class="photo cover-photo" role="img" aria-label="Photograph of the dark brick apartment building with planted balconies"></div>
    <div class="cover-rule"></div>
    <h1 class="cover-title">Studio apartments for people with<br>a psychosocial disability</h1>
    <p class="cover-address">27 Wren Lane, Carrowdale NSW 2188</p>
    <div class="cover-edge"></div>
  </section>
</div>

<!-- Inside spread -->
<div class="spread spread-two">
  <section class="page inside-left">
    <div class="photo inside-top" role="img" aria-label="Photograph of a studio kitchen and living area"></div>
    <article class="intro-box">
      <h2 class="section-title">Welcome to Carrowdale</h2>
      <p class="body-copy">Located in the heart of Carrowdale, our new 20 self-contained studio apartments which have a kitchen with fridge, small stove top and microwave, single bed, tv, dining table and bathroom. Some apartments have small balconies, and some have decks overlooking the bustling suburb.</p>
      <p class="body-copy">Situated a 5 minute walk to Carrowdale Train Station, and other public transport.</p>
    </article>
    <article class="feature-box">
      <h2 class="section-title">Communities &amp; facilities</h2>
      <ul class="feature-list">
        <li><svg class="tick"><use href="#tick"/></svg>Close to shops, cafes and public transport</li>
        <li><svg class="tick"><use href="#tick"/></svg>Local GP Practice and Dentistry</li>
        <li><svg class="tick"><use href="#tick"/></svg>Commercial Space for Social Enterprise</li>
      </ul>
      <h2 class="section-title">Features &amp; services</h2>
      <ul class="feature-list">
        <li><svg class="tick"><use href="#tick"/></svg>24/7 Video intercom &amp; on-site support</li>
        <li><svg class="tick"><use href="#tick"/></svg>Disability access walkways &amp; bathroom</li>
        <li><svg class="tick"><use href="#tick"/></svg>Trained &amp; experienced staff in psychosocial disability</li>
      </ul>
    </article>
    <div class="inside-bottom">
      <div class="photo" role="img" aria-label="Photograph of a studio living room"></div>
      <div class="photo" role="img" aria-label="Photograph of a studio with balcony doors"></div>
    </div>
  </section>

  <section class="page inside-right">
    <div class="photo bedroom-photo" role="img" aria-label="Photograph of a studio bedroom with slatted window screen"></div>
    <article class="facility-band">
      <h2 class="section-title">Communities &amp; facilities</h2>
      <ul class="feature-list">
        <li><svg class="tick"><use href="#tick"/></svg>Intercom, Security &amp; Air-Conditioning</li>
        <li><svg class="tick"><use href="#tick"/></svg>Accessible Bathroom</li>
        <li><svg class="tick"><use href="#tick"/></svg>Without Balcony</li>
        <li><svg class="tick"><use href="#tick"/></svg>Balcony Space lvl 3</li>
        <li><svg class="tick"><use href="#tick"/></svg>Juliette Balcony</li>
        <li><svg class="tick"><use href="#tick"/></svg>Standard Bathroom</li>
      </ul>
      <div class="thumbs">
        <div class="thumb" role="img" aria-label="Photograph of intercom panel"></div>
        <div class="thumb" role="img" aria-label="Photograph of balcony planting"></div>
        <div class="thumb" role="img" aria-label="Photograph of accessible bathroom"></div>
        <div class="thumb" role="img" aria-label="Photograph of courtyard"></div>
        <div class="thumb" role="img" aria-label="Photograph of balcony view"></div>
        <div class="thumb" role="img" aria-label="Photograph of standard kitchen"></div>
      </div>
    </article>
    <article class="transport-box">
      <h2 class="section-title">Public transport, shops &amp; facilities</h2>
      <p class="body-copy">Less than 5min walk to various restaurants, cafes and other shops in your local area.</p>
      <ul class="transport-list">
        <li><svg class="tick"><use href="#tick"/></svg>Corner Pharmacy – 1 min walk</li>
        <li><svg class="tick"><use href="#tick"/></svg>Supermarket – 2 min walk</li>
        <li><svg class="tick"><use href="#tick"/></svg>Fitness Centre – 2 min walk</li>
        <li><svg class="tick"><use href="#tick"/></svg>Family Medical Centre – 3 min walk</li>
        <li><svg class="tick"><use href="#tick"/></svg>Dental Practice – 4 min walk</li>
      </ul>
    </article>
    <div class="photo kitchen-photo" role="img" aria-label="Photograph of a studio kitchenette"></div>
  </section>
</div>

</body>
</html>
```